Residential Roofing Company, need a Unique business card for a Woman owned ompany

Woman Owned Residential Roofing Company. Specializing in Insurance Claims
Attention to Detail is what sets this woman owned roofing company apart from the rest
We are QORVEL Certified and are an Accredited business with an A rating with the TMK. Our Contractor License number LTW38154

```html
<!DOCTYPE html>
<html lang="en">
<head>
<meta charset="utf-8">
<title>Crestline Roofing – Business Card</title>
<link href="https://fonts.googleapis.com/css2?family=Montserrat:wght@700;800&family=Open+Sans:wght@400;600&display=swap" rel="stylesheet">
<style>
  :root {
    --backdrop: #8a8a8a;
    --paper: #ffffff;
    --navy: #1f2f6b;
    --navy-deep: #1d3063;
    --navy-soft: #3a5fa8;
    --ink-grey: #555a66;
    --badge: #1f6aa5;
  }
  * { box-sizing: border-box; margin: 0; padding: 0; }
  html, body { width: 1200px; height: 801px; overflow: hidden; }
  body {
    background: var(--backdrop);
    font-family: "Open Sans", sans-serif;
    position: relative;
  }
  .card {
    position: absolute;
    top: 252px;
    width: 525px;
    height: 300px;
    border-radius: 2px;
    overflow: hidden;
  }
  .card--front { left: 45px; background: var(--paper); border-bottom: 3px solid var(--navy); }
  .card--back { left: 630px; background: var(--navy-deep); display: flex; align-items: center; justify-content: center; }

  .brand {
    position: absolute;
    left: 30px; top: 108px;
    display: flex; align-items: center; gap: 9px;
    font-family: "Montserrat", sans-serif;
    font-weight: 800;
    font-size: 20px;
    line-height: 1;
    color: var(--navy);
    letter-spacing: -0.3px;
    text-transform: uppercase;
    white-space: nowrap;
  }
  .brand__mark { width: 16px; height: 16px; background: var(--navy); flex: none; }

  .badge {
    position: absolute; right: 24px; top: 20px;
    width: 84px; height: 32px; border-radius: 3px;
    background: var(--badge);
  }

  .person {
    position: absolute; right: 30px; top: 66px; text-align: right;
    white-space: nowrap;
  }
  .person__name {
    font-family: "Montserrat", sans-serif; font-weight: 800;
    font-size: 18px; line-height: 1.2; color: var(--navy); text-transform: uppercase;
  }
  .person__role { font-size: 13px; color: #222; }

  .divider {
    position: absolute; left: 30px; right: 30px; top: 150px;
    height: 1px; background: var(--navy);
  }
  .divider--short { top: 212px; right: 300px; }

  .address {
    position: absolute; right: 30px; top: 162px; text-align: right;
    font-style: normal;
    font-size: 13px; line-height: 1.45; color: var(--ink-grey);
  }
  .address__license { color: var(--navy); }

  .contacts {
    position: absolute; left: 30px; top: 222px;
    list-style: none; font-size: 13px; line-height: 1.4; color: var(--ink-grey);
  }
  .contacts li { display: flex; align-items: center; gap: 7px; }
  .contacts svg { width: 11px; height: 11px; fill: var(--navy); flex: none; }

  .brand--back {
    position: static;
    font-size: 34px;
    color: var(--navy-soft);
    gap: 14px;
  }
  .brand--back .brand__mark { width: 26px; height: 26px; background: var(--navy-soft); }
</style>
</head>
<body>
  <section class="card card--front" aria-label="Business card front">
    <div class="badge" role="img" aria-label="Accreditation badge"></div>

    <div class="person">
      <p class="person__name">Dana Holloway</p>
      <p class="person__role">President</p>
    </div>

    <div class="brand"><span class="brand__mark"></span>Crestline Roofing</div>

    <div class="divider"></div>

    <address class="address">
      18340 Harbor Crest Drive<br>
      Seabright CA 90417<br>
      <span class="address__license">License number LTW38154</span>
    </address>

    <div class="divider divider--short"></div>

    <ul class="contacts">
      <li><svg viewBox="0 0 24 24"><path d="M6.6 10.8a15 15 0 0 0 6.6 6.6l2.2-2.2a1 1 0 0 1 1-.25 11 11 0 0 0 3.6.6 1 1 0 0 1 1 1V20a1 1 0 0 1-1 1A17 17 0 0 1 3 4a1 1 0 0 1 1-1h3.5a1 1 0 0 1 1 1 11 11 0 0 0 .6 3.6 1 1 0 0 1-.25 1z"/></svg>555-013-4872</li>
      <li><svg viewBox="0 0 24 24"><path d="M2 5h20v14H2zM2 5l10 8 10-8v2l-10 8L2 7z"/></svg>dholloway@crestlineroofing.com</li>
      <li><svg viewBox="0 0 24 24"><circle cx="12" cy="12" r="10"/></svg>www.crestlineroofing.com</li>
    </ul>
  </section>

  <section class="card card--back" aria-label="Business card back">
    <div class="brand brand--back"><span class="brand__mark"></span>Crestline Roofing</div>
  </section>
</body>
</html>
```